Emergency Vehicle Installer and Security Firm Needs a Business Card

Our company "Corvalt" need a business card for our Emergency Vehicle Equipment Installation and Infrastructure Security Business. We are contract designers, manufacturers and installers for Emergency Vehicle Fleets. This includes installation of Emergency Lights, Sirens, Vehicle Graphics and Radio Communications. We also supply this products to an international market. We also do consultant, and installation of high level security access, alarm and surveillance equipment for medium to large size businesses.

The design should represent a level of trust in our professionalism and expertise. It should visually display our ongoing relationship with the emergency services, but not overtake our commitment to high level security options.

Target Market(s)

Emergency Services and Businesses requiring high level security

Industry/Entity Type

Business

Contact Information for Business Card

*note complete details will be given to the winning designer for revising. The name "Mark Pell will be used to fill in name".

Mark Pell
Managing Director
Corvalt NZ Limited
Phone: +64 027 604 91352
Email: mark.pell@corvalt-example.co.nz

Requirements
Must have
• Card must be in black. Using our logo on the top as supplied. Designers should try having the reverse side as a blurred image of police lights (red and blue) with our logo in greyscale in the centre (this is not particularly a requirement, but feel free to play around with this option).
Nice to have
• A card design that looks good when spot UV printed. A clean compact and graphic design. A grey scale feel on the front (excluding logo, but you can play around with that idea). Rounded smooth text.
Should not have
• Will update this section as designs come through - feel free to submit what you feel would look good.

```html
<!DOCTYPE html>
<html lang="en">
<head>
<meta charset="utf-8">
<title>Corvalt Business Card</title>
<link rel="stylesheet" href="https://fonts.googleapis.com/css2?family=Montserrat:wght@500;800&family=Arimo:wght@400&display=swap">
<style>
  :root {
    --stage: #2b2b2b;
    --card: #0b0b0b;
    --red: #e3202a;
    --white: #ffffff;
    --soft: #e6e6e6;
  }
  html, body {
    margin: 0;
    width: 1200px;
    height: 900px;
    overflow: hidden;
    background: var(--stage);
  }
  .stage {
    position: relative;
    width: 1200px;
    height: 900px;
  }
  .card {
    position: absolute;
    width: 600px;
    height: 343px;
    background: var(--card);
    border-radius: 24px;
    overflow: hidden;
    box-shadow: 0 10px 30px rgba(0,0,0,0.45);
  }
  .card--front { left: 90px; top: 80px; }
  .card--back { left: 510px; top: 477px; }

  .wordmark {
    font-family: "Montserrat", sans-serif;
    font-weight: 800;
    color: var(--white);
    letter-spacing: 1px;
    margin: 0;
    line-height: 1;
  }
  .card--front .wordmark {
    position: absolute;
    left: 0; right: 0;
    top: 140px;
    text-align: center;
    font-size: 72px;
  }
  .brand-block {
    position: absolute;
    left: 40px;
    top: 72px;
  }
  .card--back .wordmark { font-size: 54px; }
  .brand-legal {
    font-family: "Montserrat", sans-serif;
    font-weight: 500;
    font-size: 13px;
    letter-spacing: 8.5px;
    color: var(--soft);
    margin: 10px 0 0 2px;
  }
  .person {
    position: absolute;
    right: 52px;
    top: 196px;
    text-align: right;
  }
  .person__name {
    font-family: "Montserrat", sans-serif;
    font-weight: 800;
    font-size: 22px;
    color: var(--red);
    margin: 0;
    letter-spacing: 0.5px;
  }
  .person__role {
    font-family: "Arimo", sans-serif;
    font-size: 14px;
    color: var(--white);
    margin: 3px 0 0;
  }
  .card-shapes {
    position: absolute;
    inset: 0;
  }
  .contacts {
    position: absolute;
    left: 42px;
    top: 268px;
    margin: 0;
    padding: 0;
    list-style: none;
    font-family: "Arimo", sans-serif;
    font-size: 14px;
    color: var(--white);
  }
  .contacts li {
    display: flex;
    align-items: center;
    gap: 10px;
    height: 22px;
  }
  .contacts svg { width: 12px; height: 12px; }
</style>
</head>
<body>
<main class="stage">
  <section class="card card--front" aria-label="Card front">
    <p class="wordmark">CORVALT</p>
  </section>

  <section class="card card--back" aria-label="Card back">
    <svg class="card-shapes" viewBox="0 0 600 343" aria-hidden="true">
      <line x1="40" y1="258" x2="548" y2="258" stroke="var(--red)" stroke-width="2"/>
      <polygon points="0,331 348,331 372,276 382,276 358,343 0,343" fill="var(--red)"/>
      <polygon points="386,272 600,272 600,343 358,343" fill="var(--white)"/>
    </svg>

    <div class="brand-block">
      <p class="wordmark">CORVALT</p>
      <p class="brand-legal">CORVALT NZ LIMITED</p>
    </div>

    <div class="person">
      <p class="person__name">MARK PELL</p>
      <p class="person__role">Managing Director</p>
    </div>

    <ul class="contacts">
      <li>
        <svg viewBox="0 0 24 24" aria-hidden="true"><path fill="var(--red)" d="M6.6 10.8a15.1 15.1 0 0 0 6.6 6.6l2.2-2.2c.3-.3.7-.4 1-.2 1.1.4 2.3.6 3.6.6.6 0 1 .4 1 1V20c0 .6-.4 1-1 1A17 17 0 0 1 3 4c0-.6.4-1 1-1h3.5c.6 0 1 .4 1 1 0 1.3.2 2.5.6 3.6.1.3 0 .7-.2 1z"/></svg>
        <span>+64 027 604 91352</span>
      </li>
      <li>
        <svg viewBox="0 0 24 24" aria-hidden="true"><rect x="2" y="5" width="20" height="14" rx="1.5" fill="none" stroke="var(--red)" stroke-width="2.2"/><path d="M3 6l9 7 9-7" fill="none" stroke="var(--red)" stroke-width="2.2"/></svg>
        <span>mark.pell@corvalt-example.co.nz</span>
      </li>
    </ul>
  </section>
</main>
</body>
</html>
```